Brightway Tidy Services strata flyer

Looking for a flyer that will grab peoples attention also need to include some kind off promotional offer on there so they will hold onto the flyer . Would like approximateley 4 pictures of appartment blocks. Would like to include the following services. Building management Common area cleaning ,window cleaning, lawn mowing, gardening , pressure cleaning, carpet cleaning, bin cleaning. Handy man services.

Target Market(s)

appartment blocks/strata managers

Industry/Entity Type

Pressure Cleaning

Font styles to use
Serif

Colors
0355a3
ceddec
ec2027

Requirements
Must have
• company logo & colors contact details email: Info@brightwaytidyservices.example.au
• Phone: 0498305127 website brightwaytidyservices.example.au

```html
<!DOCTYPE html>
<html lang="en">
<head>
<meta charset="utf-8">
<title>Brightway Tidy Services – Strata Flyer</title>
<link rel="stylesheet" href="https://fonts.googleapis.com/css2?family=Archivo+Black&family=Archivo:wght@700;800&display=swap">
<style>
  :root {
    --brand-blue: #0355a3;
    --deep-blue: #1f4a9c;
    --fold-blue: #16357a;
    --pale-blue: #ceddec;
    --promo-red: #ec2027;
    --ink: #111111;
    --white: #ffffff;
    --sky-light: #a9d3f2;
    --sky-mid: #3f8fd6;
  }
  * { margin: 0; padding: 0; box-sizing: border-box; }
  html, body { width: 1200px; height: 2652px; overflow: hidden; background: var(--white); }
  .flyer { position: relative; width: 1200px; height: 2652px; overflow: hidden; background: var(--white); font-family: "Archivo", Arial, sans-serif; }

  .header-backdrop { position: absolute; left: 0; top: 0; width: 1200px; height: 460px;
    background: radial-gradient(ellipse at 70% 30%, var(--sky-light) 0%, var(--sky-mid) 55%, var(--brand-blue) 100%); }

  .slogan-ribbon { position: absolute; left: 0; top: 0; width: 1200px; height: 460px; }
  .slogan { position: absolute; left: 560px; top: 150px; width: 520px; text-align: center;
    color: var(--white); font-family: "Archivo", Arial, sans-serif; font-weight: 800; font-size: 78px; line-height: 96px;
    transform: rotate(-4deg); }

  .brand-mark { position: absolute; left: 24px; top: 62px; width: 400px; height: 400px; border-radius: 50%;
    background: var(--white); display: flex; align-items: center; justify-content: center; text-align: center; }
  .brand-name { color: var(--brand-blue); font-family: "Archivo Black", Arial, sans-serif; font-size: 50px; line-height: 58px; width: 320px; }

  .photo { position: absolute; }
  .photo-a { left: 0; top: 438px; width: 642px; height: 322px; background: linear-gradient(135deg, #e8ecef, #8a9aa6 60%, #3b4650); }
  .photo-b { left: 652px; top: 438px; width: 548px; height: 322px; background: linear-gradient(180deg, #b9d4ea 0%, #e9ece8 45%, #7da05c 100%); }
  .photo-c { left: 0; top: 770px; width: 642px; height: 411px; background: linear-gradient(160deg, #e6e7ea 0%, #b7aa98 50%, #5f6d4a 100%); }
  .photo-d { left: 652px; top: 770px; width: 548px; height: 411px; background: linear-gradient(180deg, #5d9be0 0%, #d8dce2 45%, #8c4f3c 80%, #2c2c2c 100%); }
  .photo-crew { left: 706px; top: 1187px; width: 494px; height: 900px;
    background: linear-gradient(90deg, rgba(255,255,255,0) 0%, #d9dee3 25%, #9aa4ad 70%, #6f7a83 100%); }

  .services { position: absolute; left: 84px; top: 1240px; }
  .services-title { color: var(--brand-blue); font-family: "Archivo Black", Arial, sans-serif; font-size: 76px; line-height: 80px; letter-spacing: 1px; }
  .services-list { list-style: none; margin-top: 38px; }
  .services-list li { color: var(--ink); font-family: "Archivo Black", Arial, sans-serif; font-size: 45px; line-height: 69.5px; padding-left: 38px; position: relative; }
  .services-list li::before { content: ""; position: absolute; left: 4px; top: 32px; width: 9px; height: 9px; border-radius: 50%; background: var(--ink); }

  .footer-band { position: absolute; left: 0; top: 2120px; width: 1200px; height: 532px;
    background: linear-gradient(180deg, rgba(206,221,236,0) 0%, var(--pale-blue) 18%, var(--pale-blue) 100%); }

  .cta-fold { position: absolute; left: 0; top: 2100px; width: 260px; height: 200px; }
  .cta-ribbon { position: absolute; left: 190px; top: 2140px; width: 1120px; height: 130px;
    background: var(--deep-blue); transform-origin: left top; transform: rotate(8.5deg);
    display: flex; align-items: center; padding-left: 70px; }
  .cta-text { color: var(--white); font-family: "Archivo", Arial, sans-serif; font-weight: 800; font-size: 44px; line-height: 1; white-space: nowrap; }

  .promo-burst { position: absolute; left: 751px; top: 1928px; width: 380px; height: 380px; }
  .promo-text { position: absolute; left: 751px; top: 2050px; width: 380px; text-align: center; color: var(--white); font-family: "Archivo Black", Arial, sans-serif; transform: rotate(-6deg); }
  .promo-text .big { display: block; font-size: 84px; line-height: 86px; }
  .promo-text .small { display: block; font-size: 40px; line-height: 46px; }

  .contact { position: absolute; left: 84px; top: 2400px; list-style: none; color: var(--brand-blue); font-family: "Archivo", Arial, sans-serif; font-weight: 800; }
  .contact li { display: flex; align-items: center; gap: 16px; }
  .contact .phone { font-size: 56px; line-height: 72px; }
  .contact .email, .contact .web { font-size: 42px; line-height: 62px; }
  .contact svg { flex: none; }
</style>
</head>
<body>
<main class="flyer">
  <div class="header-backdrop" role="img" aria-label="Water droplets on blue glass"></div>

  <svg class="slogan-ribbon" viewBox="0 0 1200 460" aria-hidden="true">
    <path d="M1130 40 L1200 70 L1200 360 L1150 300 Z" fill="var(--fold-blue)"/>
    <path d="M330 120 C620 60 900 30 1160 30 L1160 260 C900 260 640 300 330 390 Z" fill="var(--deep-blue)"/>
  </svg>
  <p class="slogan">"Experience Excellence"</p>

  <div class="brand-mark"><span class="brand-name">Brightway Tidy Services</span></div>

  <div class="photo photo-a" role="img" aria-label="Modern apartment block with louvred balconies"></div>
  <div class="photo photo-b" role="img" aria-label="White apartment buildings behind a green lawn"></div>
  <div class="photo photo-c" role="img" aria-label="Apartment block with landscaped courtyard and jacaranda"></div>
  <div class="photo photo-d" role="img" aria-label="Tall apartment tower with coloured balconies"></div>
  <div class="photo photo-crew" role="img" aria-label="Cleaners washing a glass entrance door"></div>

  <section class="services">
    <h1 class="services-title">OUR CLEANING<br>SERVICE INCLUDE:</h1>
    <ul class="services-list">
      <li>Building management</li>
      <li>Common area cleaning</li>
      <li>Window cleaning</li>
      <li>Lawn mowing</li>
      <li>Gardening</li>
      <li>Pressure cleaning</li>
      <li>Carpet cleaning</li>
      <li>Bin cleaning</li>
      <li>Handy man services</li>
    </ul>
  </section>

  <div class="footer-band"></div>

  <svg class="cta-fold" viewBox="0 2100 260 200" aria-hidden="true">
    <polygon points="55,2135 200,2142 200,2262 95,2258 140,2200" fill="var(--fold-blue)"/>
  </svg>
  <div class="cta-ribbon"><p class="cta-text">Call Us Now For Free Initial Clean</p></div>

  <svg class="promo-burst" viewBox="-140 -140 280 280" aria-hidden="true">
    <polygon fill="var(--promo-red)" stroke="#ffffff" stroke-width="5"
      points="0,-135 22,-112 52,-125 62,-94 95,-95 94,-62 125,-52 112,-22 135,0 112,22 125,52 94,62 95,95 62,94 52,125 22,112 0,135 -22,112 -52,125 -62,94 -95,95 -94,62 -125,52 -112,22 -135,0 -112,-22 -125,-52 -94,-62 -95,-95 -62,-94 -52,-125 -22,-112"/>
  </svg>
  <p class="promo-text"><span class="big">FREE</span><span class="small">QUOTES!</span></p>

  <ul class="contact">
    <li class="phone">
      <svg width="44" height="44" viewBox="0 0 24 24"><circle cx="12" cy="12" r="11" fill="none" stroke="var(--brand-blue)" stroke-width="2"/><path d="M8 6.5l2 2.5-1.2 1.5c.8 1.7 2 2.9 3.7 3.7l1.5-1.2 2.5 2-1.3 2c-4.5-.4-8.6-4.5-9-9z" fill="var(--brand-blue)"/></svg>
      <span>0498305127</span>
    </li>
    <li class="email">
      <svg width="44" height="40" viewBox="0 0 24 22"><rect x="1" y="4" width="22" height="16" rx="2" fill="var(--brand-blue)"/><path d="M2 5l10 8 10-8" fill="none" stroke="#ffffff" stroke-width="2"/></svg>
      <span>Info@brightwaytidyservices.example.au</span>
    </li>
    <li class="web">
      <svg width="44" height="44" viewBox="0 0 24 24"><circle cx="12" cy="12" r="11" fill="var(--brand-blue)"/><path d="M1 12h22M12 1c4 4 4 18 0 22M12 1c-4 4-4 18 0 22" fill="none" stroke="#ffffff" stroke-width="1.5"/></svg>
      <span>www.brightwaytidyservices.example.au</span>
    </li>
  </ul>
</main>
</body>
</html>
```